Mosvane Design

Looking for Mosvane banner and square design:
Mosvane Banner
W:1600 px H:400 px
Square
120x120

Logo attached.

Description: Data-Driven stock market portfolio management using quantitative analysis.

```html
<!DOCTYPE html>
<html lang="en">
<head>
<meta charset="utf-8">
<title>Mosvane Banner</title>
<link rel="stylesheet" href="https://fonts.googleapis.com/css2?family=Poppins:wght@400;500;700&display=swap">
<style>
  :root {
    --page: #ebebeb;
    --navy-deep: #020636;
    --navy: #06236e;
    --blue-glow: #0a47c9;
    --band-dark: #0b69c2;
    --band-light: #7cc4fb;
    --white: #ffffff;
    --shadow: rgba(0, 0, 0, 0.35);
  }
  * { margin: 0; padding: 0; box-sizing: border-box; }
  html, body {
    width: 1200px;
    height: 1200px;
    overflow: hidden;
    background: var(--page);
  }
  .canvas {
    position: relative;
    width: 1200px;
    height: 1200px;
  }
  .banner {
    position: absolute;
    left: 24px;
    top: 456px;
    width: 1153px;
    height: 287px;
    overflow: hidden;
    background: radial-gradient(ellipse 60% 95% at 53% 78%, var(--blue-glow) 0%, var(--navy) 55%, var(--navy-deep) 100%);
  }
  .banner-shadow {
    position: absolute;
    left: 100px;
    top: 743px;
    width: 1060px;
    height: 4px;
    border-radius: 50%;
    background: var(--shadow);
    filter: blur(1.5px);
  }
  .banner-art {
    position: absolute;
    inset: 0;
    width: 100%;
    height: 100%;
  }
  .tagline {
    position: absolute;
    left: 72px;
    top: 76px;
    color: var(--white);
    font-family: "Poppins", sans-serif;
    font-size: 26.5px;
    line-height: 33px;
    letter-spacing: 0.2px;
    white-space: nowrap;
  }
  .tagline-strong { font-weight: 700; display: block; }
  .tagline-light { font-weight: 400; display: block; }
  .divider {
    position: absolute;
    left: 696px;
    top: 52px;
    width: 2px;
    height: 118px;
    background: var(--white);
  }
  .brand {
    position: absolute;
    left: 714px;
    top: 78px;
    display: flex;
    align-items: center;
    gap: 18px;
  }
  .brand-dot {
    width: 62px;
    height: 62px;
    border-radius: 50%;
    background: var(--white);
  }
  .brand-name {
    color: var(--white);
    font-family: "Poppins", sans-serif;
    font-weight: 500;
    font-size: 46px;
    letter-spacing: 1.5px;
    line-height: 1;
  }
</style>
</head>
<body>
<div class="canvas">
  <div class="banner-shadow"></div>
  <section class="banner">
    <svg class="banner-art" viewBox="0 0 1153 287" preserveAspectRatio="none">
      <defs>
        <linearGradient id="particleWave" x1="0" y1="0" x2="1" y2="0">
          <stop offset="0" stop-color="#8aa6d8" stop-opacity="0.45"/>
          <stop offset="0.5" stop-color="#3f7de0" stop-opacity="0.45"/>
          <stop offset="1" stop-color="#a9c4ee" stop-opacity="0.5"/>
        </linearGradient>
        <linearGradient id="bottomBand" x1="0" y1="0" x2="1" y2="0">
          <stop offset="0" stop-color="#1473c6"/>
          <stop offset="0.45" stop-color="#7cc4fb"/>
          <stop offset="0.7" stop-color="#3a95e0"/>
          <stop offset="1" stop-color="#0566c0"/>
        </linearGradient>
      </defs>
      <path role="img" aria-label="Flowing wave of glowing data particles"
            fill="url(#particleWave)"
            d="M0 222 C120 200 220 190 330 193 C520 198 620 222 760 214 C900 206 1000 200 1153 183 L1153 244 C1000 272 850 274 720 273 C560 268 400 232 224 234 C130 236 60 244 0 250 Z"/>
      <path fill="url(#bottomBand)"
            d="M0 250 C80 240 150 234 224 234 C400 232 560 268 720 273 C850 277 1020 272 1153 244 L1153 287 L0 287 Z"/>
      <path fill="none" stroke="var(--white)" stroke-width="1.5"
            d="M0 250 C80 240 150 234 224 234 C400 232 560 268 720 273 C850 277 1020 272 1153 244"/>
    </svg>
    <h1 class="tagline">
      <span class="tagline-strong">DATA-DRIVEN STOCK MARKET PORTFOLIO</span>
      <span class="tagline-light">MANAGEMENT USING QUANTITATIVE ANALYSIS.</span>
    </h1>
    <div class="divider"></div>
    <div class="brand">
      <span class="brand-dot"></span>
      <span class="brand-name">MOSVANE</span>
    </div>
  </section>
</div>
</body>
</html>
```